SCEN Banner Ad Design

We need a banner ad design for the Scholarly Capital Exchange Network (SCEN). SCEN is an internet-based consortium whose goal is to empower the global population to invest efficiently in financial markets by learning to apply a variety of quantitative stock market prediction techniques developed by professors at top U.S. universities. These techniques have good predictive performance for different classes of financial assets comparable to large existing mutual funds in the US. With the advent of online trading platforms, an increasing number of individual investors participate in the stock market. However, most individuals lack awareness about the existence of these academic prediction methods. Also, personalized decision-making based on these methods cannot be achieved without the application of optimal quantitative tools.
SCEN makes these prediction methods, and the tools for the optimal allocation of resources between different assets, freely available to the general public through a web platform that allows the user to a) learn about the extensive research at top U.S. universities that shows financial markets have a predictable component and identify models and asset classes that suit their investment preferences and objectives; b) back test these diverse trading models, using decades of historical stock market data, that provide returns in line with top investment houses and funds; c) obtain future predictions based on the underlying models; d) update the amounts invested in each of several assets at regular intervals of time according to the predictions of these models; e) track the performance of his portfolio in real time; f) build his financial social network whereby he can gain insights from other users as well as mirror their trading strategies in real time; and g) access leading financial experts from both academia and industry, who are available to provide advice and answer questions. All of the above features are novel additions to internet-based resources available to the average user.
The banner ad will be used on several websites, but first likely on CareerLoop (a social network for job searches) and CodeHarbor (an online community for software developers/engineers). The ad should capture the theme (and SCEN’s mission) of empowering the individual investor (along with the academic emphasis of the site) and leave a little room to be able to custom tailor it to a specific user demographic. For example, on CodeHarbor the goal is to target tech savvy individuals who undertake financial investments on their own, so we will need room on the ad itself to insert a “catch phrase” that speaks to these users specifically. Similarly, on CareerLoop, we may opt to target financial asset managers and so will insert a phrase into the ad that reaches out to these types of users. You can insert a few different phrases that you come up with on different versions of the ad intended for different groups of users. Here are also a few sample "catch phrases" for you to work with:
SCEN - Control Your Investments Without The Fees
SCEN – Beat the Market. Without The Fees.
SCEN – Hack the Markets. Without the Fees.
The SCEN Beta– Hack the Ivory Tower.
SCEN – Democratizing The Investment Landscape
Finally, we are open to different color schemes, but for reference the current version of the SCEN site uses a bluish theme.
Investment

```html
<!DOCTYPE html>
<html lang="en">
<head>
<meta charset="utf-8">
<title>SCEN Banner</title>
<link href="https://fonts.googleapis.com/css2?family=Oxanium:wght@600&family=Share+Tech+Mono&family=Nunito+Sans:wght@400&display=swap" rel="stylesheet">
<style>
  :root {
    --page: #ffffff;
    --sky-top: #8a4a22;
    --sky-glow: #c9753c;
    --ridge: #1a2630;
    --tower-blue: #3f6f8f;
    --tower-dark: #0f1c27;
    --title-fill: #f4f6f8;
    --title-edge: #0c1218;
    --tagline: #d9e0e6;
    --badge-rim: #c9d2d8;
    --badge-core: #1c2a33;
  }
  html, body {
    margin: 0;
    width: 1200px;
    height: 900px;
    overflow: hidden;
    background: var(--page);
  }
  .banner {
    position: absolute;
    left: 54px;
    top: 382px;
    width: 1092px;
    height: 136px;
    overflow: hidden;
  }
  .banner-scene {
    position: absolute;
    inset: 0;
    background:
      linear-gradient(90deg, transparent 0%, transparent 42%, rgba(63,111,143,0.55) 55%, rgba(30,50,66,0.9) 72%, var(--tower-dark) 100%),
      linear-gradient(180deg, var(--sky-top) 0%, var(--sky-glow) 28%, #6b4a3a 45%, var(--ridge) 62%, #0b1218 100%);
  }
  .banner-type {
    position: absolute;
    inset: 0;
  }
  .headline {
    font-family: "Oxanium", sans-serif;
    font-weight: 600;
    font-variant: small-caps;
    fill: var(--title-fill);
    stroke: var(--title-edge);
    stroke-width: 3px;
    paint-order: stroke;
  }
  .tagline {
    font-family: "Share Tech Mono", monospace;
    fill: var(--tagline);
  }
  .cta-label {
    font-family: "Nunito Sans", sans-serif;
    fill: #ffffff;
  }
</style>
</head>
<body>
  <div class="banner">
    <div class="banner-scene" role="img" aria-label="Photo of a sunset sky over dark mountains blending into glass office towers"></div>
    <svg class="banner-type" width="1092" height="136" viewBox="0 0 1092 136">
      <defs>
        <radialGradient id="badge-face" cx="0.4" cy="0.35" r="0.7">
          <stop offset="0" stop-color="#52606a"/>
          <stop offset="1" stop-color="var(--badge-core)"/>
        </radialGradient>
      </defs>
      <text class="headline" x="9" y="80" font-size="42" textLength="952" lengthAdjust="spacingAndGlyphs">The Scholarly Capital Exchange Network</text>
      <text class="tagline" x="306" y="115" font-size="19" textLength="428" lengthAdjust="spacing">STRATEGIES IN REAL TIME</text>
      <circle class="cta-badge" cx="1026" cy="64" r="46" fill="url(#badge-face)" stroke="var(--badge-rim)" stroke-width="3"/>
      <text class="cta-label" x="970" y="124" font-size="20" textLength="113" lengthAdjust="spacing">Learn More</text>
    </svg>
  </div>
</body>
</html>
```